Business Board - PP, Stationery

KORVID Council is the leading non-profit network of value-adding board members. We work to create momentum and results in smaller and medium-sized enterprises, and to be an active and evolving networks for board members

http://korvidhub.example

I need a Powerpoint, Stationery
Updates

Target Market(s)

There are two target groups:

1) Those who are working as directors - C-level
2) The business owner who would like to have a board

Industry/Entity Type

Non-Profit

Font styles to use
Sans Serif

Requirements
Must have
• Brand essence -The soul of our brand and the core promise of what we offer
• ¥ to create momentum and results in smaller and medium-sized enterprises
• ¥ to be an active and evolving networks for board members
• Our values Fundamental principles or qualities upon which our brand is built.
• ¥ Credibility: - We keep our promises
• ¥ Integrity - We always maintain our ethical foundation
• ¥ Competence: - We always go after the "best man for the job”
• ¥ Engagement: - We get things done with empathy and willingness
• ¥ Dynamism: - We are constantly evolving
• Brand personality Characters, traits or a ributes that define our tonality and flow out of our core values.
• ¥ Modern
• ¥ Dynamic
• ¥ Cooperation
• ¥ Diversity
• ¥ Inspiration
• ¥ Quality
Nice to have
• Would like to see proposals for both PP and Stationery
Should not have
• Change in the logo

```html
<!DOCTYPE html>
<html lang="da">
<head>
<meta charset="utf-8">
<title>KORVID Council – Stationery</title>
<link rel="stylesheet" href="https://fonts.googleapis.com/css2?family=Arimo:wght@400;700&display=swap">
<style>
  :root {
    --paper: #ffffff;
    --ink: #111111;
    --muted: #a8a8a8;
    --edge: #9a9a9a;
    --blue: #00aeef;
    --green: #9ccb3b;
    --yellow: #ffc80b;
    --orange: #f58220;
    --purple: #a3238e;
  }
  * { box-sizing: border-box; margin: 0; padding: 0; }
  html, body { width: 1200px; height: 1010px; overflow: hidden; background: var(--paper); }
  body { position: relative; font-family: "Arimo", Arial, sans-serif; color: var(--ink); }

  .sheet { position: absolute; background: var(--paper); border: 1px solid #c8c8c8; }
  .brand { position: absolute; display: flex; align-items: center; }
  .brand-dot { border-radius: 50%; background: var(--blue); flex: none; }
  .brand-name { font-weight: 700; line-height: 1; letter-spacing: -0.02em; color: var(--ink); white-space: nowrap; }
  .brand-tagline { font-weight: 400; line-height: 1.1; color: var(--ink); white-space: nowrap; }

  .colour-bar { position: absolute; left: 0; right: 0; bottom: 0; display: flex; }
  .colour-bar span { flex: 1; }
  .c-blue { background: var(--blue); }
  .c-green { background: var(--green); }
  .c-yellow { background: var(--yellow); }
  .c-orange { background: var(--orange); }
  .c-purple { background: var(--purple); }

  /* Letterhead */
  .letterhead { left: 50px; top: 62px; width: 630px; height: 891px; }
  .letterhead .brand { left: 76px; top: 54px; gap: 10px; }
  .letterhead .brand-dot { width: 30px; height: 30px; }
  .letterhead .brand-name { font-size: 28px; }
  .letterhead .brand-tagline { font-size: 11px; margin-top: 2px; }
  .letterhead .colour-bar { height: 11px; }
  .letterhead .web-vertical {
    position: absolute; right: 12px; bottom: 22px;
    writing-mode: vertical-rl; transform: rotate(180deg);
    font-size: 14px; color: var(--muted); letter-spacing: 0.02em;
  }

  /* Envelope */
  .envelope { left: 338px; top: 286px; width: 740px; height: 328px; border-right: none; }
  .envelope-flap { position: absolute; left: 1077px; top: 286px; width: 76px; height: 328px; }
  .envelope .brand { left: 38px; top: 38px; gap: 9px; }
  .envelope .brand-dot { width: 26px; height: 26px; }
  .envelope .brand-name { font-size: 24px; }
  .envelope .brand-tagline { font-size: 9.5px; margin-top: 2px; }
  .envelope .colour-bar { height: 8px; }
  .envelope .web { position: absolute; right: 12px; bottom: 13px; font-size: 14px; color: var(--muted); }

  /* Business card */
  .business-card { left: 732px; top: 687px; width: 267px; height: 154px; border-color: #555; }
  .business-card .brand { left: 12px; top: 38px; gap: 5px; }
  .business-card .brand-dot { width: 14px; height: 14px; }
  .business-card .brand-name { font-size: 11.5px; }
  .business-card .brand-tagline { font-size: 4.6px; margin-top: 1px; }
  .business-card .colour-bar { height: 4px; }
  .card-person { position: absolute; left: 143px; top: 39px; }
  .card-name { font-size: 10px; font-weight: 700; line-height: 1.1; }
  .card-role { font-size: 7px; line-height: 1.2; }
  .card-contact { position: absolute; left: 143px; top: 80px; list-style: none; font-size: 7.4px; line-height: 9.6px; }
</style>
</head>
<body>

  <section class="sheet letterhead" aria-label="Letterhead">
    <div class="brand">
      <span class="brand-dot"></span>
      <div>
        <div class="brand-name">KORVID Council</div>
        <div class="brand-tagline">værdiskabende bestyrelsesarbejde</div>
      </div>
    </div>
    <div class="web-vertical">korvidhub.example</div>
    <div class="colour-bar"><span class="c-blue"></span><span class="c-green"></span><span class="c-yellow"></span><span class="c-orange"></span><span class="c-purple"></span></div>
  </section>

  <section class="sheet envelope" aria-label="Envelope">
    <div class="brand">
      <span class="brand-dot"></span>
      <div>
        <div class="brand-name">KORVID Council</div>
        <div class="brand-tagline">værdiskabende bestyrelsesarbejde</div>
      </div>
    </div>
    <div class="web">korvidhub.example</div>
    <div class="colour-bar"><span class="c-blue"></span><span class="c-green"></span><span class="c-yellow"></span><span class="c-orange"></span><span class="c-purple"></span></div>
  </section>
  <svg class="envelope-flap" viewBox="0 0 76 328" aria-hidden="true">
    <path d="M0 0.5 H24 Q42 0.5 46 20 L75 164 L46 308 Q42 327.5 24 327.5 H0" fill="#fff" stroke="#a0a0a0" stroke-width="1"/>
  </svg>

  <section class="sheet business-card" aria-label="Business card">
    <div class="brand">
      <span class="brand-dot"></span>
      <div>
        <div class="brand-name">KORVID Council</div>
        <div class="brand-tagline">værdiskabende bestyrelsesarbejde</div>
      </div>
    </div>
    <div class="card-person">
      <div class="card-name">Name Will Go Here</div>
      <div class="card-role">Designation</div>
    </div>
    <ul class="card-contact">
      <li>Office Address</li>
      <li>Cell Number</li>
      <li>Fax Number</li>
      <li>E-mail address</li>
      <li>socialnet/youridhere</li>
      <li>korvidhub.example</li>
    </ul>
    <div class="colour-bar"><span class="c-purple"></span><span class="c-orange"></span><span class="c-yellow"></span><span class="c-green"></span><span class="c-blue"></span></div>
  </section>

</body>
</html>
```